Thistlewood Group Business Card Design

We are looking for a new business card design, we are not happy with our current design. We are a boutique management consulting firm and our clients are typically meridian 400 companies.

I have attached the current front and back that we have as well as a version of our logo that can be used. I am trying to get a higher resolution version of the logo file to upload to the project.

Target Market(s)

Meridian 400 companies are our primary client base. Financial services, life sciences, pharmaceuticals and telecom companies are

Industry/Entity Type

Management Consulting

Contact Information for Business Card

We are trying to communicate a high degree of professionalism, a somewhat minimalist perhaps with some air of whimsy (without overdoing it). Attached is the current design, front and back as well as logos. I like the current back of the card and assume we will keep the phrase the same.

From a color palette perspective, I prefer to stay with a gray scale as they are today.

Font styles to use
Sans Serif

Colors
1b1b1b
474747
ffffff

Requirements
Must have
• Two sided business card design. File format should be something that can be used outside of Photoshop like MS Publisher so that they can be edited with personal information.
• Font should be calibri or something very similar and should be available within MS Office
Should not have
• No other logos or graphics outside of the logo provided.

```html
<!DOCTYPE html>
<html lang="en">
<head>
<meta charset="utf-8">
<title>Thistlewood Group Business Card</title>
<link rel="stylesheet" href="https://fonts.googleapis.com/css2?family=Carlito:wght@400;700&display=swap">
<style>
  :root {
    --card: #1b1b1b;
    --silver: #474747;
    --ink: #ffffff;
    --muted: #d9d9d9;
    --backdrop: #4a413d;
  }
  * { margin: 0; padding: 0; box-sizing: border-box; }
  html, body {
    width: 1200px; height: 787px; overflow: hidden;
    background: var(--backdrop);
    font-family: "Carlito", "Calibri", sans-serif;
  }
  .stage {
    position: relative; width: 1200px; height: 787px;
  }
  .card {
    position: absolute; width: 540px; height: 309px;
    background: var(--card); color: var(--ink);
    box-shadow: 0 10px 30px rgba(0,0,0,.45);
  }
  .card--tagline { left: 40px; top: 239px; }
  .card--contact { left: 620px; top: 239px; }

  .brand { display: flex; align-items: center; gap: 12px; position: absolute; }
  .brand__dot { width: 30px; height: 30px; border-radius: 50%; }
  .brand__name { font-weight: 700; line-height: 1; letter-spacing: .5px; }

  .card--tagline .brand { left: 60px; top: 48px; }
  .card--tagline .brand__dot { background: var(--silver); }
  .card--tagline .brand__name { color: var(--silver); font-size: 58px; }
  .tagline {
    position: absolute; left: 60px; top: 150px;
    font-weight: 700; font-size: 27px; line-height: 1.15; text-align: center;
    width: 330px;
  }
  .website {
    position: absolute; left: 60px; top: 236px;
    font-size: 15px; letter-spacing: 1.5px; color: var(--muted);
  }

  .card--contact .brand { left: 150px; top: 44px; }
  .card--contact .brand__dot { background: var(--ink); }
  .card--contact .brand__name { font-size: 56px; color: var(--ink); }
  .tm { position: absolute; font-size: 10px; color: var(--muted); }
  .card--contact .tm { left: 505px; top: 52px; }
  .card--tagline .tm { left: 440px; top: 56px; color: var(--silver); }

  .contact {
    position: absolute; top: 150px; left: 0; width: 100%;
    display: flex; font-size: 17px; line-height: 1.3;
  }
  .contact__person { width: 262px; text-align: right; padding-right: 16px; }
  .contact__divider { width: 1px; background: var(--muted); opacity: .7; height: 118px; }
  .contact__office { padding-left: 16px; }
  .contact__name { font-weight: 700; font-size: 19px; }
</style>
</head>
<body>
<main class="stage">
  <section class="card card--tagline" aria-label="Card back">
    <div class="brand">
      <span class="brand__dot"></span>
      <span class="brand__name">Thistlewood</span>
    </div>
    <span class="tm">TM</span>
    <p class="tagline">The preferred choice<br>for leadership’s top priorities</p>
    <p class="website">www.ThistlewoodGroup.com</p>
  </section>

  <section class="card card--contact" aria-label="Card front">
    <div class="brand">
      <span class="brand__dot"></span>
      <span class="brand__name">Thistlewood</span>
    </div>
    <span class="tm">TM</span>
    <div class="contact">
      <div class="contact__person">
        <p class="contact__name">Ellis Marsh</p>
        <p>Los Angeles Office</p>
        <p>Managing Director</p>
        <p>Tel : 206.555.0147</p>
        <p>emarsh@thistlewoodgroup.com</p>
      </div>
      <div class="contact__divider"></div>
      <div class="contact__office">
        <p>Thistlewood Group, Inc.</p>
        <p>Headquarters</p>
        <p>218 Harbor Lane</p>
        <p>Suite 103</p>
        <p>Cedar Is., WA 98000</p>
      </div>
    </div>
  </section>
</main>
</body>
</html>
```